Educational outcome management software startup firm needs a graphic design

Our software startup firm, Pelvar Insight Technologies recently purchased a beautiful logo from Brushmarket (uploaded file). We are now looking for a graphic design to be used in the marketing activities of Pelvar Insight Technologies. See the uploaded picture of what a sketch of the graphic we are looking for.

```html
<!DOCTYPE html>
<html lang="en">
<head>
<meta charset="utf-8">
<title>Pelvar Insight Technologies – Learner Outcome Ecosystem</title>
<link href="https://fonts.googleapis.com/css2?family=Oswald:wght@400;500&display=swap" rel="stylesheet">
<style>
  :root {
    --red: #d03c2f;
    --navy: #1b2a4e;
    --ink: #141414;
    --paper: #ffffff;
  }
  html, body { margin: 0; padding: 0; overflow: hidden; background: var(--paper); }
  .canvas { width: 1200px; height: 848px; position: relative; overflow: hidden; background: var(--paper); }
  .ecosystem { position: absolute; inset: 0; }
  .ring { fill: none; stroke: var(--navy); stroke-width: 1.5; }
  .ring--dashed { stroke-dasharray: 4 3; stroke-width: 1.2; }
  .node--red { fill: var(--red); }
  .node--navy { fill: var(--navy); }
  .node-edge { stroke: var(--paper); stroke-width: 3; }
  .skill { fill: var(--paper); stroke-width: 1.6; }
  .skill--red { stroke: var(--red); }
  .skill--navy { stroke: var(--navy); }
  text { font-family: "Oswald", "Arial Narrow", sans-serif; font-weight: 500; text-transform: uppercase; }
  .label-outer { fill: var(--ink); font-size: 14px; }
  .label-node { fill: var(--paper); font-size: 10.5px; text-anchor: middle; }
  .label-skill { fill: var(--ink); font-size: 10.5px; text-anchor: middle; }
  .learner { fill: var(--red); }
  .brand { position: absolute; left: 978px; top: 756px; display: flex; align-items: center; gap: 8px; }
  .brand-mark { width: 12px; height: 12px; background: var(--red); }
  .brand-name { font-family: "Oswald", "Arial Narrow", sans-serif; font-weight: 500; font-size: 15px; color: var(--navy); letter-spacing: 0.3px; }
</style>
</head>
<body>
<div class="canvas">
  <svg class="ecosystem" width="1200" height="848" viewBox="0 0 1200 848">
    <!-- rings -->
    <circle class="ring" cx="600" cy="426" r="263"/>
    <circle class="ring ring--dashed" cx="600" cy="426" r="270"/>
    <circle class="ring" cx="600" cy="426" r="181"/>
    <circle class="ring" cx="600" cy="426" r="104"/>

    <!-- stakeholders -->
    <g class="stakeholders">
      <circle class="node--red node-edge" cx="600" cy="162" r="32" role="img" aria-label="Parent and guardian icon"/>
      <circle class="node--navy node-edge" cx="786" cy="238" r="32" role="img" aria-label="Employer icon"/>
      <circle class="node--red node-edge" cx="862" cy="426" r="32" role="img" aria-label="Graduation cap icon"/>
      <circle class="node--navy node-edge" cx="786" cy="610" r="32" role="img" aria-label="Government building icon"/>
      <circle class="node--red node-edge" cx="600" cy="688" r="32" role="img" aria-label="Market storefront icon"/>
      <circle class="node--navy node-edge" cx="414" cy="610" r="32" role="img" aria-label="School administrator shield icon"/>
      <circle class="node--red node-edge" cx="338" cy="426" r="32" role="img" aria-label="Counselling session icon"/>
      <circle class="node--navy node-edge" cx="414" cy="238" r="32" role="img" aria-label="Teacher at board icon"/>
    </g>
    <g class="stakeholder-labels">
      <text class="label-outer" x="605" y="104" text-anchor="middle"><tspan x="605">Parent/</tspan><tspan x="605" dy="16">Guardian</tspan></text>
      <text class="label-outer" x="838" y="242">Employer</text>
      <text class="label-outer" x="914" y="422"><tspan x="914">Post Secondary</tspan><tspan x="914" dy="16">Education System</tspan></text>
      <text class="label-outer" x="832" y="619">Government</text>
      <text class="label-outer" x="598" y="745" text-anchor="middle"><tspan x="598">International</tspan><tspan x="598" dy="16">Market Place</tspan></text>
      <text class="label-outer" x="369" y="611" text-anchor="end"><tspan x="369">School</tspan><tspan x="369" dy="16">Administrator</tspan></text>
      <text class="label-outer" x="290" y="420" text-anchor="end"><tspan x="290">School/</tspan><tspan x="290" dy="16">Counsler</tspan></text>
      <text class="label-outer" x="360" y="239" text-anchor="end">Teacher</text>
    </g>

    <!-- milestones -->
    <g class="milestones">
      <circle class="node--red" cx="511" cy="266" r="42"/>
      <text class="label-node" x="511" y="270">Entrepreneur</text>
      <circle class="node--navy" cx="693" cy="270" r="42"/>
      <text class="label-node" y="260"><tspan x="693">High</tspan><tspan x="693" dy="13">School</tspan><tspan x="693" dy="13">Graduation</tspan></text>
      <circle class="node--red" cx="781" cy="428" r="42"/>
      <text class="label-node" x="781" y="432">Employment</text>
      <circle class="node--navy" cx="688" cy="582" r="42"/>
      <text class="label-node" y="577"><tspan x="688">Admission into</tspan><tspan x="688" dy="13">Post-Secondary</tspan><tspan x="688" dy="13">Institution</tspan></text>
      <circle class="node--red" cx="507" cy="580" r="42"/>
      <text class="label-node" y="573"><tspan x="507">Completion</tspan><tspan x="507" dy="13">into Elementary</tspan><tspan x="507" dy="13">School</tspan></text>
      <circle class="node--navy" cx="419" cy="422" r="42"/>
      <text class="label-node" y="415"><tspan x="419">Graduation</tspan><tspan x="419" dy="13">from Higher</tspan><tspan x="419" dy="13">Education</tspan></text>
    </g>

    <!-- skills -->
    <g class="skills">
      <circle class="skill skill--red" cx="611" cy="326" r="35"/>
      <text class="label-skill" y="324"><tspan x="611">Reading</tspan><tspan x="611" dy="13">Skills</tspan></text>
      <circle class="skill skill--navy" cx="692" cy="384" r="35"/>
      <text class="label-skill" y="382"><tspan x="692">Writing</tspan><tspan x="692" dy="13">Skills</tspan></text>
      <circle class="skill skill--red" cx="682" cy="485" r="35"/>
      <text class="label-skill" y="483"><tspan x="682">Study</tspan><tspan x="682" dy="13">Skills</tspan></text>
      <circle class="skill skill--navy" cx="592" cy="530" r="35"/>
      <text class="label-skill" y="525"><tspan x="592">Information</tspan><tspan x="592" dy="12">Technology</tspan><tspan x="592" dy="12">Skills</tspan></text>
      <circle class="skill skill--red" cx="509" cy="465" r="35"/>
      <text class="label-skill" y="463"><tspan x="509">Social</tspan><tspan x="509" dy="13">Skills</tspan></text>
      <circle class="skill skill--navy" cx="519" cy="366" r="35"/>
      <text class="label-skill" y="364"><tspan x="519">STEM</tspan><tspan x="519" dy="13">Skills</tspan></text>
    </g>

    <!-- learner at centre -->
    <rect class="learner" x="558" y="376" width="86" height="94" rx="30" role="img" aria-label="Student reading a book"/>
  </svg>

  <div class="brand">
    <span class="brand-mark"></span>
    <span class="brand-name">Pelvar Insight Technologies</span>
  </div>
</div>
</body>
</html>
```